Glintly Starter Pack

We are going live with our new cleaning business, this week. It is a cleaning business with a twist: a fully digital cleaning business, where customers can book online or via an app.
I have written a starter pack to give to the cleaners to help them understand the do's and don'ts of our business, what the products are, and importantly, how to accept a job using our app.
All i need is for this information to be put into a nice looking, brochure format.
Industry/Entity Type
Digital
Look and feel
Each slider illustrates characteristics of the customer's brand and the style your logo design should communicate.

```html
<!DOCTYPE html>
<html lang="en">
<head>
<meta charset="utf-8">
<title>Glintly Starter Pack – Cover Spread</title>
<link rel="stylesheet" href="https://fonts.googleapis.com/css2?family=Montserrat:wght@400;600;700&display=swap">
<style>
  :root {
    --backdrop: #a3a3a3;
    --paper: #f7f7f7;
    --paper-shade: #ececec;
    --motif-blue: #c7dfea;
    --brand-blue: #5b9fd6;
    --rule-gold: #e2bf2a;
    --ink-dark: #3a3a3a;
    --ink-muted: #555555;
    --accent-magenta: #b5245e;
  }
  * { margin: 0; padding: 0; box-sizing: border-box; }
  html, body {
    width: 1200px;
    height: 800px;
    overflow: hidden;
    background: var(--backdrop);
    font-family: "Montserrat", Arial, sans-serif;
  }
  .cover-spread {
    position: absolute;
    left: 120px;
    top: 110px;
    width: 960px;
    height: 570px;
    box-shadow: 0 12px 30px rgba(0,0,0,0.25);
  }
  .cover-art {
    position: absolute;
    inset: 0;
    width: 960px;
    height: 570px;
  }
  .back-cover__legal {
    position: absolute;
    left: 30px;
    top: 522px;
    font-size: 7.5px;
    color: var(--ink-muted);
    letter-spacing: 0.1px;
  }
  .front-cover__web {
    position: absolute;
    left: 512px;
    top: 509px;
    font-size: 13px;
    font-weight: 700;
    letter-spacing: 0.6px;
    color: var(--ink-dark);
  }
  .brand-lockup {
    position: absolute;
    left: 822px;
    top: 408px;
    width: 120px;
    display: flex;
    flex-direction: column;
    align-items: center;
  }
  .brand-lockup__dot {
    width: 54px;
    height: 54px;
    border-radius: 50%;
    background: var(--brand-blue);
    margin-bottom: 8px;
  }
  .brand-lockup__name {
    font-size: 32px;
    font-weight: 700;
    color: var(--ink-dark);
    line-height: 1;
  }
</style>
</head>
<body>
  <main class="cover-spread">
    <svg class="cover-art" viewBox="0 0 960 570" xmlns="http://www.w3.org/2000/svg">
      <defs>
        <clipPath id="spread-clip"><rect x="0" y="0" width="960" height="570"/></clipPath>
        <linearGradient id="spine-shade" x1="0" x2="1">
          <stop offset="0" stop-color="#000" stop-opacity="0"/>
          <stop offset="0.5" stop-color="#000" stop-opacity="0.08"/>
          <stop offset="1" stop-color="#000" stop-opacity="0"/>
        </linearGradient>
        <path id="title-arc" d="M 752 246 A 400 400 0 0 0 830 52"/>
      </defs>
      <rect class="page page--back" x="0" y="0" width="480" height="570" fill="var(--paper)"/>
      <rect class="page page--front" x="480" y="0" width="480" height="570" fill="var(--paper)"/>
      <g clip-path="url(#spread-clip)">
        <circle class="brand-motif" role="img" aria-label="Large soft blue brand motif" cx="440" cy="225" r="345" fill="var(--motif-blue)"/>
      </g>
      <rect class="spine" x="455" y="0" width="50" height="570" fill="url(#spine-shade)"/>
      <line class="rule rule--back" x1="0" y1="496" x2="480" y2="496" stroke="var(--rule-gold)" stroke-width="3"/>
      <line class="rule rule--front" x1="480" y1="496" x2="808" y2="496" stroke="var(--rule-gold)" stroke-width="3"/>
      <line class="rule rule--edge" x1="952" y1="496" x2="960" y2="496" stroke="var(--rule-gold)" stroke-width="3"/>
      <text class="front-cover__title" font-family="Montserrat, Arial, sans-serif" font-size="15" letter-spacing="7" fill="var(--accent-magenta)">
        <textPath href="#title-arc">STARTER PACK</textPath>
      </text>
    </svg>

    <p class="back-cover__legal">© 2014 // Glintly Pty Limited. Corporate identity manuals &amp; guides document. All Right Reserved.®</p>
    <p class="front-cover__web">WWW.GLINTLY.COM.AU</p>
    <div class="brand-lockup">
      <span class="brand-lockup__dot"></span>
      <span class="brand-lockup__name">Glintly</span>
    </div>
  </main>
</body>
</html>
```